Real Estate "For Sale" Sign for construction company

We need a sign that we can use to hang on a post and place on the road when we sell a property. The sign will be simple and will need to mainly feature our logo (files attached), as well as the words "For Sale", and then our phone number "(555) 617 3489". The sign will hang on a post that'll look something like the attached picture.

Target Market(s)

Home buyers

Industry/Entity Type

Real Estate

Font styles to use
Serif
Sans Serif

Colors
0054AA
0677BA
7BADD7
CADEEF
E8F1F8
0094D4
00A9DD
6FCCEA
C7EBF8
E9F6FB

Requirements
Must have
• For Sale & our phone number

```html
<!DOCTYPE html>
<html lang="en">
<head>
<meta charset="utf-8">
<title>Ridgeline Harbor Homes – For Sale Sign</title>
<link rel="stylesheet" href="https://fonts.googleapis.com/css2?family=Montserrat:wght@400;800&display=swap">
<style>
  :root {
    --sky: #8ed7f6;
    --brand-blue: #1a7fc1;
    --deep-blue: #0a4fa3;
    --navy: #131f4b;
    --cyan: #1aa3de;
    --white: #ffffff;
  }
  html, body {
    margin: 0;
    padding: 0;
    width: 828px;
    height: 1200px;
    overflow: hidden;
    background: var(--sky);
  }
  .sign {
    display: block;
    width: 828px;
    height: 1200px;
    font-family: "Montserrat", Arial, sans-serif;
  }
  .sign__sky { fill: var(--sky); }
  .sign__wave { fill: var(--deep-blue); }
  .sign__panel { fill: var(--navy); }
  .brand__mark { fill: var(--brand-blue); }
  .brand__name {
    fill: var(--brand-blue);
    font-weight: 400;
    font-size: 70px;
  }
  .brand__tagline {
    fill: var(--brand-blue);
    font-weight: 400;
    font-size: 21px;
  }
  .headline {
    fill: var(--white);
    font-weight: 800;
    font-size: 138px;
  }
  .contact__label {
    fill: var(--deep-blue);
    font-weight: 800;
    font-size: 45px;
  }
  .contact__rule { stroke: var(--deep-blue); stroke-width: 3; }
  .contact__phone {
    fill: var(--deep-blue);
    font-weight: 800;
    font-size: 104px;
  }
  .footer__stripe { fill: var(--cyan); }
  .footer__band { fill: var(--deep-blue); }
</style>
</head>
<body>
<svg class="sign" viewBox="0 0 828 1200" xmlns="http://www.w3.org/2000/svg">
  <rect class="sign__sky" width="828" height="1200"/>

  <!-- top wave and main panel -->
  <path class="sign__wave" d="M0 239 C70 234 150 246 230 250 C300 252 350 240 414 240 C480 240 520 252 600 254 C690 256 760 240 828 239 L828 700 L0 700 Z"/>
  <path class="sign__panel" d="M0 264 C80 256 160 268 240 266 C320 264 360 248 414 248 C470 248 520 264 600 266 C690 268 760 258 828 262 L828 699 C700 690 560 684 414 684 C270 684 130 690 0 698 Z"/>

  <!-- bottom curved band -->
  <path class="sign__wave" d="M0 698 C130 690 270 684 414 684 C560 684 700 690 828 699 L828 748 C700 706 560 684 414 684 C270 684 130 706 0 748 Z"/>

  <!-- brand -->
  <g class="brand">
    <circle class="brand__mark" cx="414" cy="112" r="62"/>
    <text class="brand__name" x="50" y="232" textLength="728" lengthAdjust="spacingAndGlyphs">Ridgeline Harbor</text>
    <text class="brand__tagline" x="222" y="291" textLength="379" lengthAdjust="spacing">HOMES</text>
  </g>

  <!-- headline -->
  <text class="headline" x="52" y="522" textLength="718" lengthAdjust="spacingAndGlyphs">FOR SALE</text>

  <!-- contact -->
  <g class="contact">
    <text class="contact__label" x="233" y="892" textLength="357" lengthAdjust="spacingAndGlyphs">CALL OR TEXT</text>
    <line class="contact__rule" x1="115" y1="907" x2="711" y2="907"/>
    <text class="contact__phone" x="82" y="1040" textLength="657" lengthAdjust="spacingAndGlyphs">555 617 3489</text>
  </g>

  <!-- footer -->
  <rect class="footer__stripe" x="0" y="1156" width="828" height="10"/>
  <rect class="footer__band" x="0" y="1164" width="828" height="36"/>
</svg>
</body>
</html>
```